Wholesale in Gold Jewellery & Gold Bullion

We are an established gold jewellery and gold bullion wholesaler selling these products to international clients. We already have a name and logo of our company, hence please view attached current card design. We need a completely new design to compliment our business and industry and the final design should be new and elegant.

Contact Information for Business Card

New card details must be same as per current card. Like logo, name, tel no. & etc.

Colors

Designer to choose colors to be used in the design.

```html
<!DOCTYPE html>
<html lang="en">
<head>
<meta charset="utf-8">
<title>Ravello &amp; Co – Business Card</title>
<link rel="stylesheet" href="https://fonts.googleapis.com/css2?family=Playfair+Display:wght@900&family=Lora:wght@400;500&family=Lobster&display=swap">
<style>
  :root {
    --stage: #2a2a2a;
    --ink: #141414;
    --ink-soft: #1d1d1d;
    --paper: #ffffff;
    --gold-dark: #a8801d;
    --gold: #d6b13c;
    --gold-light: #f6e58a;
    --gold-grad: linear-gradient(115deg, var(--gold-dark) 0%, var(--gold) 30%, var(--gold-light) 55%, var(--gold) 75%, var(--gold-dark) 100%);
  }
  * { margin: 0; padding: 0; box-sizing: border-box; }
  html, body { width: 1200px; height: 895px; overflow: hidden; background: var(--stage); }
  .canvas { position: relative; width: 1200px; height: 895px; }

  .card {
    position: absolute;
    left: 250px;
    width: 700px;
    height: 400px;
    overflow: hidden;
    box-shadow: 0 12px 30px rgba(0,0,0,.5);
  }

  /* Back side */
  .card-back { top: 28px; background: var(--ink); }
  .back-brand {
    position: absolute; left: 0; right: 0; top: 0; bottom: 0;
    display: flex; flex-direction: column; align-items: center; justify-content: center; gap: 18px;
  }
  .back-brand .brand-dot {
    width: 70px; height: 70px; border-radius: 50%; background: var(--gold-grad);
  }
  .back-brand .brand-name {
    font-family: "Playfair Display", serif; font-weight: 900;
    font-size: 26px; letter-spacing: 1px; color: var(--gold);
  }

  /* Front side */
  .card-front { top: 467px; background: var(--paper); }
  .front-logo-dot {
    position: absolute; left: 48px; top: 130px;
    width: 108px; height: 108px; border-radius: 50%; background: var(--gold-grad);
  }
  .company-name {
    position: absolute; right: 34px; top: 70px;
    font-family: "Playfair Display", serif; font-weight: 900;
    font-size: 44px; letter-spacing: 1px; color: var(--ink);
    white-space: nowrap;
  }
  .contact-band {
    position: absolute; left: 0; right: 0; top: 250px; height: 108px;
    background: var(--ink-soft);
  }
  .title-banner {
    position: absolute; right: 0; top: 172px; width: 330px; height: 88px;
    background: var(--gold-grad);
    clip-path: polygon(0 0, 100% 0, 100% 100%, 8% 100%);
    border-left: 3px solid var(--paper);
  }
  .title-banner .person-name {
    position: absolute; right: 26px; top: 14px;
    font-family: "Lobster", cursive; font-size: 33px; color: var(--ink);
  }
  .title-banner .person-role {
    position: absolute; right: 26px; top: 56px;
    font-family: "Lora", serif; font-size: 14px; color: var(--ink);
  }
  .address {
    position: absolute; right: 26px; top: 280px;
    font-family: "Lora", serif; font-size: 15px; color: var(--paper);
  }
  .contact-list {
    position: absolute; left: 40px; top: 262px;
    list-style: none;
    font-family: "Lora", serif; font-size: 15px; color: var(--paper);
  }
  .contact-list li { display: flex; align-items: center; gap: 12px; height: 22px; }
  .contact-list svg { width: 14px; height: 14px; fill: var(--gold); flex: none; }
</style>
</head>
<body>
<main class="canvas">

  <section class="card card-back" aria-label="Card back">
    <div class="back-brand">
      <span class="brand-dot"></span>
      <span class="brand-name">RAVELLO &amp; CO</span>
    </div>
  </section>

  <section class="card card-front" aria-label="Card front">
    <span class="front-logo-dot"></span>
    <h1 class="company-name">RAVELLO &amp; CO PTE LTD</h1>

    <div class="contact-band"></div>

    <div class="title-banner">
      <p class="person-name">Arjun Mehravan</p>
      <p class="person-role">Director</p>
    </div>

    <p class="address">12 Harlow Lane, Singapore 100234</p>

    <ul class="contact-list">
      <li>
        <svg viewBox="0 0 14 14"><path d="M4 0h6a1 1 0 0 1 1 1v12a1 1 0 0 1-1 1H4a1 1 0 0 1-1-1V1a1 1 0 0 1 1-1zm0 2v9h6V2z"/></svg>
        +65 9100 2345
      </li>
      <li>
        <svg viewBox="0 0 14 14"><path d="M1 4c2-3 10-3 12 0l-2 2-2-1V4H5v1L3 6zM3 7h8l1 6H2z"/></svg>
        +65 6100 4000
      </li>
      <li>
        <svg viewBox="0 0 14 14"><path d="M3 0h8v4H3zM1 5h12v6h-2V9H3v2H1zM4 10h6v4H4z"/></svg>
        +65 6200 1188
      </li>
      <li>
        <svg viewBox="0 0 14 14"><path d="M0 3h14v8H0zm1 1 6 4 6-4v-.2L7 7 1 3.8z"/></svg>
        arjun@ravelloco.com
      </li>
    </ul>
  </section>

</main>
</body>
</html>
```